Legal Postcard for Carlvista Film Works

LEGAL VIDEO SERVICES- Expert & Lay Witness Depositions- Day in the Life Videos- Security & Surveillance Video Editing- Onsite Video Documentation- Ability to make bad video clearer- Focus Groups & Video Monitoring- Video Conversion and Duplication- Over 15 Years of Legal Video Experience

Phone: 418.562.7391
Email: Walter@Carlvista.example

Target Market(s)

Law Firms

Industry/Entity Type

Legal

Font styles to use
Serif

Requirements
Must have
• The information in my description, my logo & picture.
• Nice design touches and accents
• Return address & Logo on mailing side of postcard, all other info on the main side
• Colors should be consistent with my logo

```html
<!DOCTYPE html>
<html lang="en">
<head>
<meta charset="utf-8">
<title>Carlvista Film Works – Legal Postcard</title>
<link rel="stylesheet" href="https://fonts.googleapis.com/css2?family=Open+Sans:ital,wght@0,400;0,600;0,700;1,400;1,600&family=Oswald:wght@500;600&display=swap">
<style>
  :root {
    --royal: #1c3fd0;
    --royal-deep: #0f2a9e;
    --royal-light: #3d63ea;
    --silver: #c9cdd4;
    --silver-dark: #8d939c;
    --paper: #ffffff;
    --mist: #eef0f3;
    --ink: #3a3d44;
    --stage: #e4e2de;
  }
  * { box-sizing: border-box; margin: 0; padding: 0; }
  html, body { width: 867px; height: 1200px; overflow: hidden; }
  body { background: var(--stage); font-family: "Open Sans", Arial, sans-serif; position: relative; }

  .card { position: absolute; left: 36px; width: 795px; background: var(--paper); overflow: hidden; box-shadow: 0 4px 14px rgba(0,0,0,.25); }
  .card--front { top: 24px; height: 588px; }
  .card--back { top: 632px; height: 544px; background: linear-gradient(135deg, var(--paper) 40%, var(--mist)); }

  .card__art { position: absolute; inset: 0; width: 100%; height: 100%; }

  .brand-name { position: absolute; font-family: "Open Sans", Arial, sans-serif; font-weight: 700; color: var(--royal); }
  .front__brand { left: 540px; top: 60px; font-size: 38px; display: flex; align-items: center; gap: 12px; }
  .front__brand .brand-dot { width: 22px; height: 22px; border-radius: 50%; background: var(--royal); }

  .headline { position: absolute; right: 32px; text-align: right; color: var(--paper); white-space: nowrap; }
  .headline__lead { top: 226px; font-size: 42px; font-weight: 400; font-style: italic; }
  .headline__main { top: 282px; font-family: "Oswald", Arial, sans-serif; font-weight: 600; font-size: 46px; line-height: 60px; }
  .headline__main .cap { font-size: 58px; }
  .headline__sub { top: 360px; right: 48px; font-size: 20px; font-weight: 600; font-style: italic; }

  .services { position: absolute; top: 420px; list-style: none; color: var(--paper); font-size: 13px; font-weight: 600; line-height: 22px; white-space: nowrap; }
  .services--left { right: 300px; text-align: right; }
  .services--right { left: 516px; }
  .services li { display: flex; align-items: center; gap: 7px; }
  .services--left li { justify-content: flex-end; }
  .services li::before { content: ""; width: 5px; height: 5px; border-radius: 50%; background: var(--paper); flex: none; }
  .services--left li::before { order: 2; }

  .front__web { position: absolute; left: 26px; bottom: 30px; font-size: 18px; color: var(--ink); }

  .back__brand { left: 468px; top: 38px; font-size: 26px; font-weight: 600; }
  .return-address { position: absolute; left: 468px; top: 76px; font-size: 14px; line-height: 20px; color: var(--ink); font-style: normal; }
  .stamp-box { position: absolute; left: 698px; top: 36px; width: 70px; height: 70px; background: var(--silver); }
  .address-lines { position: absolute; left: 470px; top: 330px; width: 300px; }
  .address-lines span { display: block; height: 1px; background: var(--silver-dark); margin-bottom: 36px; }

  .contact { position: absolute; left: 26px; color: var(--paper); }
  .contact__phone { top: 414px; font-size: 30px; font-weight: 600; display: flex; align-items: center; gap: 12px; }
  .contact__phone svg { width: 26px; height: 26px; }
  .contact__email { top: 466px; font-size: 18px; }
  .contact__web { top: 500px; font-size: 18px; letter-spacing: 1.5px; }
</style>
</head>
<body>

<section class="card card--front" aria-label="Postcard front">
  <svg class="card__art" viewBox="0 0 795 588">
    <defs>
      <linearGradient id="bandGrad" x1="0" y1="0" x2="1" y2="1">
        <stop offset="0" stop-color="#2a4fe0"/>
        <stop offset="1" stop-color="#0f2a9e"/>
      </linearGradient>
      <radialGradient id="heroPhoto" cx=".45" cy=".5" r=".6">
        <stop offset="0" stop-color="#c7b8a8"/>
        <stop offset=".55" stop-color="#9a8a7c"/>
        <stop offset="1" stop-color="#3b3532"/>
      </radialGradient>
      <linearGradient id="ringGrad" x1="0" y1="0" x2="1" y2="1">
        <stop offset="0" stop-color="#f4f5f7"/>
        <stop offset=".5" stop-color="#a8adb5"/>
        <stop offset="1" stop-color="#e6e8ec"/>
      </linearGradient>
    </defs>
    <path d="M0,440 C200,300 480,215 795,150 L795,560 C560,520 260,490 0,500 Z" fill="url(#bandGrad)"/>
    <path d="M0,440 C200,300 480,215 795,150 L795,172 C490,238 220,320 0,462 Z" fill="#3d63ea" opacity=".7"/>
    <circle cx="200" cy="100" r="188" fill="url(#heroPhoto)" role="img" aria-label="Photo of a videographer crouching with a camera"/>
    <circle cx="200" cy="100" r="196" fill="none" stroke="url(#ringGrad)" stroke-width="16"/>
  </svg>

  <div class="brand-name front__brand"><span class="brand-dot"></span>Carlvista</div>

  <p class="headline headline__lead">Over 15 Years of</p>
  <h1 class="headline headline__main"><span class="cap">L</span>egal Video Experience</h1>
  <p class="headline headline__sub">Legal Video Services</p>

  <ul class="services services--left">
    <li>Ability to make bad video clearer</li>
    <li>Focus Groups &amp; Video Monitoring</li>
    <li>Video Conversion and Duplication</li>
  </ul>
  <ul class="services services--right">
    <li>Expert &amp; Lay Witness Depositions</li>
    <li>Day in the Life Videos</li>
    <li>Security &amp; Surveillance Video Editing</li>
    <li>Onsite Video Documentation</li>
  </ul>

  <p class="front__web">www.carlvista.example</p>
</section>

<section class="card card--back" aria-label="Postcard mailing side">
  <svg class="card__art" viewBox="0 0 795 544">
    <defs>
      <radialGradient id="portraitPhoto" cx=".5" cy=".45" r=".6">
        <stop offset="0" stop-color="#c9b2a4"/>
        <stop offset=".5" stop-color="#a0413d"/>
        <stop offset="1" stop-color="#2a2224"/>
      </radialGradient>
      <linearGradient id="ringGradBack" x1="0" y1="0" x2="1" y2="1">
        <stop offset="0" stop-color="#f4f5f7"/>
        <stop offset=".5" stop-color="#9aa0a8"/>
        <stop offset="1" stop-color="#e6e8ec"/>
      </linearGradient>
    </defs>
    <path d="M440,544 C560,400 680,330 795,300 L795,330 C690,360 580,430 480,544 Z" fill="#dfe2e7" opacity=".8"/>
    <path d="M0,385 L300,385 C360,385 400,430 430,544 L0,544 Z" fill="#1c3fd0"/>
    <circle cx="215" cy="200" r="168" fill="url(#portraitPhoto)" role="img" aria-label="Photo of the videographer smiling behind a video camera"/>
    <circle cx="215" cy="200" r="176" fill="none" stroke="url(#ringGradBack)" stroke-width="16"/>
  </svg>

  <h2 class="brand-name back__brand">Carlvista</h2>
  <address class="return-address">Harlow Bend, MN 55990<br>United States</address>
  <div class="stamp-box" aria-label="Stamp area"></div>
  <div class="address-lines" aria-hidden="true"><span></span><span></span><span></span><span></span></div>

  <p class="contact contact__phone">
    <svg viewBox="0 0 24 24" aria-hidden="true"><rect x="0" y="0" width="24" height="24" rx="4" fill="#fff"/><path d="M7 5c1 0 2 2.5 2 3s-1 1-1 1.5c.5 2 2.5 4 4.5 4.5.5 0 1-1 1.5-1s3 1 3 2-1.5 3-3 3C9 18 6 15 6 8.5 6 6.5 6.5 5 7 5z" fill="#1c3fd0"/></svg>
    418.562.7391
  </p>
  <p class="contact contact__email">Walter@Carlvista.example</p>
  <p class="contact contact__web">www.carlvista.example</p>
</section>

</body>
</html>
```